Rebrand our dated accomodation business website "Tallowind Quay Residences"

we have a wordpress website ( www.tallowindquay.com.au) that is old and out dated .
I will need a new updated SQUARESPACE website (in which i already have ) with a fresh new design , also new logo and an easy site to manage from my end.
Need to connect our socials - facebook and instagram and our new site
Check out "brindle cove landing" for inspiration...
These apartments are consists of -
-One bedroom One bath
-Two bedroom One bath
-Two bedroom Two bath
-Three bedroom Two bath
all other information is on our current website
KEEP it simple and fresh
ALSO WE DONT HAVE HUGE BIG BOATS IN THE MARINA SO PLEASE DONT HAVE THAT IN THE LOGO

Target Market(s)

Anyone looking for accomodation !! we have 64 rooms !!

Industry/Entity Type

accomodation / short stays

Coding

Coded - Design and coding required

Number of Pages Required

5+ page

Requirements
Must have
• Fresh , modern and easy to use.....have a hoilday vibe , also use natural colours
Nice to have
• i like accomodation website like ....https://fernandgrove.com.au/luxury-coastal-accommodation/ or https://theorvellainn.com/
Should not have
• please do not use bright colours and scripted fonts

```html
<!DOCTYPE html>
<html lang="en">
<head>
<meta charset="utf-8">
<title>Tallowind Quay Residences</title>
<link href="https://fonts.googleapis.com/css2?family=Jost:wght@300;400;500&display=swap" rel="stylesheet">
<style>
:root{
  --navy:#13293a;
  --navy-mid:#1f3b54;
  --band:#2a4862;
  --ink:#1d3346;
  --muted:#7d8790;
  --light:#f5f6f7;
  --gold:#e2a63a;
  --white:#ffffff;
}
*{box-sizing:border-box;margin:0;padding:0}
html,body{width:1200px;height:5314px;overflow:hidden}
body{font-family:"Jost",sans-serif;color:var(--ink);background:var(--white);position:relative}
section,header,footer{position:absolute;left:0;width:1200px}
.abs{position:absolute}
.heading{font-weight:400;letter-spacing:.16em;text-transform:uppercase}
.btn{position:absolute;background:var(--navy-mid);color:var(--white);font-size:15px;letter-spacing:.18em;text-transform:uppercase;display:flex;align-items:center;justify-content:center;font-weight:500}
.photo{position:absolute}

/* hero */
.hero{top:0;height:728px;background:linear-gradient(180deg,#5d7fa6 0%,#a9bfd3 25%,#d8dcd8 45%,#9aa89a 62%,#6d8a6d 72%,#2f86c4 86%,#1d6fae 100%)}
.topbar .social{position:absolute;top:14px;display:flex;gap:20px;left:85px}
.topbar .social span{width:12px;height:12px;border-radius:50%;background:var(--white);display:block}
.phone-top{position:absolute;right:85px;top:12px;color:var(--white);font-size:15px;letter-spacing:.1em;display:flex;gap:8px;align-items:center}
.brand{position:absolute;left:85px;top:60px;color:var(--white);font-size:13px;letter-spacing:.2em;text-align:center;width:130px}
.brand .mark{width:28px;height:28px;border:1.5px solid var(--white);margin:0 auto 8px}
.nav{position:absolute;left:303px;top:86px;display:flex;gap:30px;color:var(--white);font-size:15px;letter-spacing:.14em}
.menu-icon{position:absolute;left:906px;top:85px;width:22px}
.menu-icon i{display:block;height:2px;background:var(--white);margin-bottom:5px}
.booking{left:993px;top:74px;width:122px;height:42px}
.hero h1{position:absolute;left:85px;top:562px;width:860px;color:var(--white);font-size:42px;font-weight:400;letter-spacing:.04em;line-height:51px;text-transform:uppercase}
.see-more{left:952px;top:614px;width:162px;height:46px}

/* about */
.about{top:728px;height:825px}
.about .photo-main{left:85px;top:49px;width:455px;height:726px;background:linear-gradient(160deg,#3f7cc6 0%,#8fb4e0 35%,#e9ecef 55%,#4e7d3c 75%,#2d5522 100%)}
.about h2{position:absolute;left:617px;top:68px;font-size:37px;line-height:44px;letter-spacing:.18em}
.about p{position:absolute;left:617px;top:176px;width:496px;font-size:13px;line-height:24px;color:#57636d;font-weight:300}
.read-more{left:617px;top:367px;width:178px;height:44px}
.about .illus{left:690px;top:440px;width:340px;height:360px;background:radial-gradient(ellipse at 50% 85%,#e4ebf1 0%,#f4f7f9 45%,#ffffff 70%)}

/* accommodation */
.accom{top:1553px;height:1202px;background:var(--navy);color:var(--white)}
.accom h2{position:absolute;left:85px;top:112px;font-size:36px;letter-spacing:.2em}
.accom .intro{position:absolute;left:615px;top:43px;width:500px;font-size:13px;line-height:24px;font-weight:300}
.room{position:absolute;width:502px}
.room .pic{height:347px}
.room .label{display:flex;justify-content:space-between;margin-top:26px;font-size:20px;letter-spacing:.14em;text-transform:uppercase}
.room .label a{font-size:14px;color:var(--white);text-decoration:underline;letter-spacing:.14em;font-weight:500;margin-top:5px}

/* testimonial */
.review{top:2755px;height:569px;text-align:center}
.review .quote{position:absolute;left:570px;top:80px}
.review h3{position:absolute;top:152px;width:100%;font-size:22px;font-weight:400}
.stars{position:absolute;top:182px;left:534px;display:flex;gap:6px}
.review .body{position:absolute;left:190px;top:230px;width:820px;font-size:17px;line-height:35px;color:var(--muted);font-weight:300}
.review .name{position:absolute;top:436px;width:100%;font-size:17px;letter-spacing:.1em;color:#444}
.review .src{position:absolute;top:466px;width:100%;font-size:13px;color:var(--muted)}
.arrow{position:absolute;top:272px}

/* harbour */
.harbour{top:3324px;height:924px;background:var(--navy);color:var(--white);text-align:center}
.harbour h2{position:absolute;top:76px;width:100%;font-size:36px;letter-spacing:.2em}
.harbour .intro{position:absolute;left:130px;top:133px;width:940px;font-size:13px;line-height:24px;font-weight:300}
.card{position:absolute;top:260px;width:326px;text-align:left}
.card .pic{height:362px}
.card h4{margin-top:40px;font-size:18px;font-weight:400;letter-spacing:.12em}
.card p{margin-top:12px;font-size:13px;line-height:24px;font-weight:300}
.card a{display:block;margin-top:12px;color:var(--white);font-size:14px;font-weight:500;letter-spacing:.14em;text-decoration:underline}
.dots{position:absolute;top:838px;left:562px;display:flex;gap:22px}
.dots span{width:10px;height:10px;border-radius:50%;border:1.5px solid var(--white)}
.dots span.on{background:var(--white)}

/* partners */
.partners{top:4248px;height:528px}
.badge{position:absolute;top:226px;height:70px}
.map{left:526px;top:66px;width:588px;height:396px;background:linear-gradient(135deg,#dfeee0 0%,#e8efe3 50%,#a9d3ea 78%,#7dbfe4 100%)}

/* book band */
.band{top:4776px;height:111px;background:var(--band);overflow:hidden}
.band .ring{position:absolute;border-radius:50%;border:26px solid rgba(255,255,255,.06)}
.band h2{position:absolute;left:240px;top:33px;color:var(--white);font-size:36px;letter-spacing:.2em}
.band .book{position:absolute;left:790px;top:32px;width:171px;height:46px;border:1.5px solid var(--white);color:var(--white);font-size:14px;letter-spacing:.18em;display:flex;align-items:center;justify-content:center}

/* footer */
.footer{top:4887px;height:427px}
.foot-brand{position:absolute;left:100px;top:120px;width:232px;text-align:center}
.foot-brand .mark{width:56px;height:56px;border:2px solid var(--ink);margin:0 auto 14px}
.foot-brand .name{font-size:16px;letter-spacing:.2em;color:var(--ink)}
.foot-brand .sub{font-size:9px;letter-spacing:.3em;color:var(--muted);margin-top:12px}
.foot-social{position:absolute;left:161px;top:222px;display:flex;gap:12px}
.foot-social span{width:44px;height:44px;border-radius:50%;border:1px solid #d3d8dc;display:flex;align-items:center;justify-content:center}
.foot-social i{width:12px;height:12px;background:var(--ink);border-radius:2px;display:block}
.col{position:absolute;top:78px}
.col h5{font-size:14px;font-weight:400;letter-spacing:.18em;color:var(--ink);margin-bottom:40px}
.col li{list-style:none;font-size:13px;color:#5d6770;line-height:33px;display:flex;gap:12px;align-items:center}
.copy{position:absolute;top:373px;left:85px;width:1030px;display:flex;align-items:center;font-size:12px;color:#5d6770}
.copy .rule{flex:1;height:1px;background:#cfd5da;margin:0 16px}
</style>
</head>
<body>

<header class="hero">
  <div class="topbar">
    <div class="social"><span></span><span></span><span></span></div>
    <div class="phone-top"><svg width="14" height="14" viewBox="0 0 24 24" fill="#fff"><path d="M6.6 10.8a15 15 0 0 0 6.6 6.6l2.2-2.2a1 1 0 0 1 1-.25 11.4 11.4 0 0 0 3.6.6 1 1 0 0 1 1 1V20a1 1 0 0 1-1 1A17 17 0 0 1 3 4a1 1 0 0 1 1-1h3.5a1 1 0 0 1 1 1c0 1.25.2 2.45.6 3.6a1 1 0 0 1-.25 1z"/></svg>1800 555 214</div>
  </div>
  <div class="brand"><div class="mark"></div>TALLOWIND QUAY</div>
  <nav class="nav"><span>HOME</span><span>ABOUT US</span><span>OUR LOCATION</span><span>NEWS</span><span>CONTACT US</span></nav>
  <div class="menu-icon"><i></i><i></i><i></i></div>
  <div class="btn booking">Booking</div>
  <h1>Contemporary self contained apartments Brindle Cove Jetty precinct</h1>
  <div class="btn see-more">See more</div>
  <div class="abs" role="img" aria-label="Photograph of the apartment complex with pool and gardens" style="inset:0;z-index:-1"></div>
</header>

<section class="about">
  <div class="photo photo-main" role="img" aria-label="Photograph of the white apartment building with palms and entry sign"></div>
  <h2 class="heading">About Tallowind<br>Quay Residences</h2>
  <p>Tallowind Quay Residences is a modern accommodation complex situated in the heart of Brindle Cove's vibrant Jetty precinct. The complex comprises 64 fully self-contained, privately owned apartments spread across three stories. Guests can choose from spacious 1, 2, or 3-bedroom apartments, each featuring modern decor, full kitchens, air-conditioned living areas, and private balconies or patios. Amenities include free Wi-Fi, StreamBox, secure undercover parking, and direct lift access to all apartments.</p>
  <div class="btn read-more">Read more</div>
  <div class="photo illus" role="img" aria-label="Illustration of a couple travelling with a suitcase"></div>
</section>

<section class="accom">
  <h2 class="heading">Accommodation</h2>
  <div class="intro">Whether you're visiting for an event or enjoying a well-earned vacation, we have the perfect apartment waiting just for you.<br>Singles and couples can savour cocktail hour from the comfort of their private balcony or patio.<br>Families will love the freedom to relax in their own space and prepare meals in a fully equipped kitchen.<br>Corporate guests will feel right at home with secure surroundings, undercover parking, and all the comforts of a spacious, welcoming apartment.</div>
  <div class="room" style="left:85px;top:282px"><div class="pic" role="img" aria-label="Photograph of the one bedroom apartment bedroom" style="background:linear-gradient(135deg,#e9e6e1,#b6a48e 70%,#7a5a3c)"></div><div class="label"><span>1 Bedroom Apartment</span><a>Book now</a></div></div>
  <div class="room" style="left:612px;top:282px"><div class="pic" role="img" aria-label="Photograph of the two bedroom apartment bedroom" style="background:linear-gradient(135deg,#d8c3a6,#c7a47a 50%,#6e3f22)"></div><div class="label"><span>2 Bedroom Apartment</span><a>Book now</a></div></div>
  <div class="room" style="left:85px;top:738px"><div class="pic" role="img" aria-label="Photograph of the three bedroom apartment bedroom" style="background:linear-gradient(135deg,#cbb89c,#e6dccd 50%,#8a6d50)"></div><div class="label"><span>3 Bedroom Apartment</span><a>Book now</a></div></div>
  <div class="room" style="left:612px;top:738px"><div class="pic" role="img" aria-label="Photograph of the executive suite bedroom with ocean view" style="background:linear-gradient(135deg,#8ea9c2,#d9cdb9 50%,#4a3426)"></div><div class="label"><span>Executive 3 Bedroom Suite</span><a>Book now</a></div></div>
</section>

<section class="review">
  <svg class="quote" width="60" height="42" viewBox="0 0 60 42" fill="none" stroke="#3b5670" stroke-width="2"><path d="M26 4C12 6 4 16 4 28a9 9 0 1 0 9-9M56 4C42 6 34 16 34 28a9 9 0 1 0 9-9"/></svg>
  <h3>We Will Definitely Stay Again</h3>
  <div class="stars">
    <svg width="20" height="20" viewBox="0 0 24 24" fill="#e2a63a"><path d="M12 2l3 7 7 .6-5.3 4.7 1.6 7.2L12 17.8 5.7 21.5l1.6-7.2L2 9.6 9 9z"/></svg>
    <svg width="20" height="20" viewBox="0 0 24 24" fill="#e2a63a"><path d="M12 2l3 7 7 .6-5.3 4.7 1.6 7.2L12 17.8 5.7 21.5l1.6-7.2L2 9.6 9 9z"/></svg>
    <svg width="20" height="20" viewBox="0 0 24 24" fill="#e2a63a"><path d="M12 2l3 7 7 .6-5.3 4.7 1.6 7.2L12 17.8 5.7 21.5l1.6-7.2L2 9.6 9 9z"/></svg>
    <svg width="20" height="20" viewBox="0 0 24 24" fill="#e2a63a"><path d="M12 2l3 7 7 .6-5.3 4.7 1.6 7.2L12 17.8 5.7 21.5l1.6-7.2L2 9.6 9 9z"/></svg>
    <svg width="20" height="20" viewBox="0 0 24 24" fill="#e2a63a"><path d="M12 2l3 7 7 .6-5.3 4.7 1.6 7.2L12 17.8 5.7 21.5l1.6-7.2L2 9.6 9 9z"/></svg>
  </div>
  <p class="body">Great place, close to beach, jetty restaurants and attractions, petrel island. It was a nice spacious apartment. With good size bathrooms and great laundry and a full size kitchen. The view out over the pool and gardens was really nice and relaxing. The balcony was really big to air clothes out on or sit around the large table. The beds were comfortable and really nice to sleep in.<br><span style="display:block;margin-top:10px">We will definitely try and stay there again when we come up next time.</span></p>
  <div class="name">DANIEL</div>
  <div class="src">Online Review</div>
  <svg class="arrow" style="left:84px" width="14" height="28" viewBox="0 0 14 28" fill="none" stroke="#a8b4c0" stroke-width="2"><path d="M12 2L2 14l10 12"/></svg>
  <svg class="arrow" style="left:1102px" width="14" height="28" viewBox="0 0 14 28" fill="none" stroke="#1d3346" stroke-width="2"><path d="M2 2l10 12L2 26"/></svg>
</section>

<section class="harbour">
  <h2 class="heading">About Brindle Cove</h2>
  <p class="intro">Visitors to Brindle Cove have the chance to explore a truly spectacular destination—where stunning beaches meet lush rainforests and scenic hinterland.<br>A true vacation paradise, "the Cove" offers something for everyone. Stay up to date with the latest attractions and events by checking our blog regularly.<br>Brindle Cove is also home to a world-class International Sports Stadium, hosting a wide range of exciting events throughout the year</p>
  <div class="card" style="left:68px"><div class="pic" role="img" aria-label="Photograph of the one bedroom bathroom" style="background:linear-gradient(160deg,#8d8f90,#d9d9d6 50%,#a5a7a6)"></div><h4>ONE BEDROOM ONE BATH</h4><p>Fancy a cold one with a side of Brindle Cove's laid-back charm? Check out our Brindle Cove Breweries tour for an awesome day out!</p><a>READ MORE</a></div>
  <div class="card" style="left:437px"><div class="pic" role="img" aria-label="Photograph of the two bedroom one bath bedroom" style="background:linear-gradient(160deg,#d9c7ad,#efe9df 50%,#2e3f6a)"></div><h4>TWO BEDROOM ONE BATH</h4><p>The Brindle Coast transforms into one of Australia's premier destinations for whale watching each year. Here's how to get the best experience.</p><a>READ MORE</a></div>
  <div class="card" style="left:804px"><div class="pic" role="img" aria-label="Photograph of the two bedroom two bath hallway" style="background:linear-gradient(160deg,#bca586,#e6ddd0 50%,#7c6448)"></div><h4>TWO BEDROOM TWO BATH</h4><p>Few experiences capture the beauty of the Brindle Coast better than renowned coastal walks. The Skerry Point Coastal Walk stands out.</p><a>READ MORE</a></div>
  <div class="dots"><span class="on"></span><span></span><span></span></div>
</section>

<section class="partners">
  <div class="badge" style="left:98px;width:120px;background:#e8ecef;border-radius:6px" role="img" aria-label="Accredited business badge"></div>
  <div class="badge" style="left:244px;width:124px;background:#e8ecef;border-radius:6px" role="img" aria-label="Tourism quality badge"></div>
  <div class="badge" style="left:392px;width:112px;background:#e8ecef;border-radius:50%" role="img" aria-label="Review listing badge"></div>
  <div class="photo map" role="img" aria-label="Map of Brindle Cove showing the apartment location and nearby attractions"></div>
</section>

<section class="band">
  <div class="ring" style="left:-70px;top:-40px;width:190px;height:190px"></div>
  <div class="ring" style="left:1010px;top:-40px;width:190px;height:190px"></div>
  <h2 class="heading">Book direct &amp; save!</h2>
  <div class="book">BOOK NOW</div>
</section>

<footer class="footer">
  <div class="foot-brand"><div class="mark"></div><div class="name">TALLOWIND QUAY</div><div class="sub">RESIDENCES</div></div>
  <div class="foot-social"><span><i></i></span><span><i></i></span></div>
  <div class="col" style="left:437px"><h5>QUICK LINKS</h5><ul><li>Home</li><li>About Us</li><li>Accommodation</li><li>Our Location</li><li>News/Events</li><li>Contact Us</li></ul></div>
  <div class="col" style="left:668px"><h5>CONTACT INFO</h5><ul>
    <li><svg width="16" height="12" viewBox="0 0 16 12" fill="none" stroke="#1d3346"><rect x=".5" y=".5" width="15" height="11"/><path d="M.5.5L8 7l7.5-6.5"/></svg>sales@tallowindquay.com.au</li>
    <li><svg width="16" height="16" viewBox="0 0 24 24" fill="none" stroke="#1d3346" stroke-width="1.5"><path d="M6.6 10.8a15 15 0 0 0 6.6 6.6l2.2-2.2 4.6 1.4V20A17 17 0 0 1 4 4h3.5l1.4 4.6z"/></svg>1800 555 214</li>
    <li><svg width="16" height="16" viewBox="0 0 24 24" fill="none" stroke="#1d3346" stroke-width="1.5"><path d="M6.6 10.8a15 15 0 0 0 6.6 6.6l2.2-2.2 4.6 1.4V20A17 17 0 0 1 4 4h3.5l1.4 4.6z"/></svg>(02) 5550 1382</li></ul></div>
  <div class="col" style="left:1000px"><h5>OTHER LINKS</h5><ul><li>Terms &amp; Conditions</li><li>Privacy Policy</li><li>Site Admin</li></ul></div>
  <div class="copy"><span>© 2026 <b style="font-weight:500">Tallowind Quay Residences.</b> All right reserved.</span><span class="rule"></span><span>June 02, 2026. Layout_4</span></div>
</footer>

</body>
</html>
```